Commercial Office Fitout company needs a simple website

We need a website for our company Tallow Bridge (QLD) Pty Ltd. We are in the construction industry and we specialise in commercial office fitouts (partitions/glass/doors). Our company colours are black and silver. Please use our logo attached.
We only need an "about us" section, a "portfolio" section where we display some pictures of our work, and a "contact us" section. We would like our website to be simple, effective, professional and modern.

Industry/Entity Type

Construction

Number of Pages Required

1 page

```html
<!DOCTYPE html>
<html lang="en">
<head>
<meta charset="utf-8">
<title>Tallow Bridge (QLD) Pty Ltd</title>
<link href="https://fonts.googleapis.com/css2?family=Lato:wght@300;400;700;900&family=Roboto:wght@400&display=swap" rel="stylesheet">
<style>
  :root {
    --ink: #111111;
    --text: #222222;
    --muted: #555555;
    --silver: #9a9a9a;
    --line: #b9b9b9;
    --panel: #1b1b1b;
    --white: #ffffff;
    --footer: #0c0c0c;
  }
  * { box-sizing: border-box; margin: 0; padding: 0; }
  html, body { width: 1200px; height: 2998px; overflow: hidden; background: var(--white); }
  body { position: relative; font-family: "Lato", sans-serif; color: var(--text); }
  .abs { position: absolute; }

  /* brand lockup */
  .brand { text-align: center; color: var(--ink); font-family: "Lato", sans-serif; font-weight: 900; }
  .brand-mark { display: block; margin: 0 auto; background: var(--ink); }
  .brand-name { display: block; letter-spacing: 2px; line-height: 1.1; }
  .brand-sub { display: block; letter-spacing: 3px; line-height: 1.2; }

  .site-brand { left: 400px; top: 22px; width: 400px; }
  .site-brand .brand-mark { width: 58px; height: 58px; }
  .site-brand .brand-name { font-size: 34px; margin-top: 20px; }
  .site-brand .brand-sub { font-size: 16px; }

  /* navigation */
  .main-nav { left: 0; top: 212px; width: 1200px; display: flex; justify-content: center; gap: 78px; }
  .main-nav a { font-size: 19px; letter-spacing: 4px; color: var(--text); text-decoration: none; text-transform: uppercase; font-weight: 400; }

  /* section headings */
  .section-title { font-weight: 900; font-size: 38px; letter-spacing: 8px; text-transform: uppercase; color: var(--ink); text-align: center; }
  .title-rule { height: 2px; background: var(--ink); }

  /* about */
  .about-title { left: 60px; top: 424px; width: 620px; }
  .about-text { left: 90px; top: 518px; width: 560px; text-align: center; font-size: 19px; line-height: 25.5px; font-weight: 400; }
  .about-brand { left: 720px; top: 424px; width: 300px; }
  .about-brand .brand-mark { width: 64px; height: 64px; }
  .about-brand .brand-name { font-size: 32px; margin-top: 18px; }
  .about-brand .brand-sub { font-size: 15px; }
  .about-reflection { left: 720px; top: 580px; width: 300px; opacity: .16; transform: scaleY(-1); filter: blur(2px); }
  .about-reflection .brand-mark { width: 64px; height: 64px; }
  .about-reflection .brand-name { font-size: 32px; margin-bottom: 18px; }
  .about-reflection .brand-sub { font-size: 15px; }

  /* numbers band */
  .numbers-photo { left: 0; top: 770px; width: 1200px; height: 404px;
    background: linear-gradient(90deg, #4a2a22 0%, #7a3a2a 20%, #a34a3a 40%, #6a5a58 60%, #8a4030 80%, #3a2a24 100%); }
  .numbers-panel { left: 48px; top: 786px; width: 1104px; height: 388px; background: var(--panel); color: var(--white); }
  .numbers-title { left: 0; top: 26px; width: 1104px; color: var(--white); font-size: 40px; }
  .numbers-rule { left: 420px; top: 78px; width: 264px; background: var(--white); height: 1px; }
  .numbers-text { left: 220px; top: 84px; width: 664px; text-align: center; font-size: 17px; line-height: 23px; }
  .stat { top: 180px; text-align: center; }
  .stat-value { font-size: 124px; font-weight: 700; line-height: 1; letter-spacing: -2px; }
  .stat-rule { width: 120px; height: 1px; background: #666; margin: 22px auto 0; }
  .stat-label { font-size: 21px; margin-top: 14px; font-weight: 400; }
  .stat-dot { top: 238px; width: 22px; height: 22px; border-radius: 50%; background: #3a3a3a; }

  /* portfolio */
  .portfolio-title { left: 0; top: 1222px; width: 1200px; }
  .portfolio-rule { left: 470px; top: 1270px; width: 240px; }
  .portfolio-watermark { left: 440px; top: 1290px; width: 320px; opacity: .14; filter: blur(3px); }
  .portfolio-watermark .brand-mark { width: 80px; height: 80px; }
  .portfolio-watermark .brand-name { font-size: 36px; margin-top: 18px; }
  .portfolio-watermark .brand-sub { font-size: 16px; }

  .portfolio-grid { left: 48px; top: 1460px; width: 1104px; display: grid; grid-template-columns: repeat(4, 270px); grid-auto-rows: 270px; gap: 8px; }
  .work-photo { background: linear-gradient(180deg, #e9ecee 0%, #cfd3d4 35%, #7d7770 55%, #4b4845 80%, #2f2e2d 100%); }
  .work-feature { background: linear-gradient(180deg, #2a2a2a, #151515); color: var(--white); text-align: center; padding-top: 20px; }
  .work-feature-kicker { font-size: 19px; letter-spacing: 4px; font-weight: 400; }
  .work-feature .brand { color: var(--white); margin-top: 22px; }
  .work-feature .brand-mark { width: 44px; height: 44px; background: var(--white); }
  .work-feature .brand-name { font-size: 24px; margin-top: 12px; }
  .work-feature .brand-sub { font-size: 12px; }
  .work-feature-link { display: inline-block; margin-top: 40px; font-size: 15px; color: #dddddd; text-decoration: underline; }

  /* contact */
  .contact-title { left: 0; top: 2358px; width: 1200px; }
  .contact-rule { left: 478px; top: 2406px; width: 244px; }
  .field-label { font-family: "Roboto", sans-serif; font-size: 22px; color: #333; }
  .field-box { border: 2px solid #c9c9c9; background: var(--white); }
  .contact-brand { left: 730px; top: 2482px; width: 300px; }
  .contact-brand .brand-mark { width: 64px; height: 64px; }
  .contact-brand .brand-name { font-size: 32px; margin-top: 18px; }
  .contact-brand .brand-sub { font-size: 15px; }
  .contact-details { left: 750px; top: 2636px; font-size: 19px; line-height: 27px; color: var(--text); font-style: normal; }
  .contact-line { display: flex; align-items: center; gap: 16px; }
  .contact-line svg { width: 20px; height: 20px; margin-left: 2px; }

  /* footer */
  .site-footer { left: 0; top: 2944px; width: 1200px; height: 54px; background: var(--footer); color: var(--white); text-align: center; font-size: 19px; line-height: 54px; }
</style>
</head>
<body>

<header>
  <div class="abs brand site-brand">
    <span class="brand-mark"></span>
    <span class="brand-name">TALLOW BRIDGE</span>
    <span class="brand-sub">(QLD) PTY LTD</span>
  </div>
  <nav class="abs main-nav">
    <a href="#home">Home</a>
    <a href="#about">About</a>
    <a href="#portfolio">Portfolio</a>
    <a href="#contact">Contact Us</a>
  </nav>
</header>

<section id="about">
  <h1 class="abs section-title about-title">We are Tallow Bridge</h1>
  <p class="abs about-text">Lorem ipsum dolor sit amet, consectetur adipiscing elit. Duis at ex massa. Quisque consectetur nisi non nulla congue, ut imperdiet erat sollicitudin. Suspendisse vel hendrerit lacus, vitae hendrerit nisl. Nam sagittis vulputate luctus. Vestibulum commodo iaculis purus. Fusce laoreet massa at nulla pharetra placerat.</p>
  <div class="abs brand about-brand">
    <span class="brand-mark"></span>
    <span class="brand-name">TALLOW BRIDGE</span>
    <span class="brand-sub">(QLD) PTY LTD</span>
  </div>
  <div class="abs brand about-reflection" aria-hidden="true">
    <span class="brand-mark"></span>
    <span class="brand-name">TALLOW BRIDGE</span>
    <span class="brand-sub">(QLD) PTY LTD</span>
  </div>
</section>

<section id="numbers">
  <div class="abs numbers-photo" role="img" aria-label="Blurred photograph of an office interior behind the statistics panel"></div>
  <div class="abs numbers-panel">
    <h2 class="abs section-title numbers-title">Let the numbers speak</h2>
    <div class="abs numbers-rule"></div>
    <p class="abs numbers-text">Lorem ipsum dolor sit amet, consectetur adipiscing elit. Duis at ex massa. Quisque consectetur nisi non nulla congue, ut imperdiet erat sollicitudin. Suspendisse vel hendrerit lacus, vitae hendrerit nisl. Nam sagittis vulputate luctus. Vestibulum commodo iaculis purus.</p>

    <div class="abs stat" style="left:-4px; width:180px;">
      <div class="stat-value">124</div><div class="stat-rule"></div>
      <div class="stat-label">Number of projects</div>
    </div>
    <span class="abs stat-dot" style="left:227px;"></span>
    <div class="abs stat" style="left:310px; width:200px;">
      <div class="stat-value">54</div><div class="stat-rule"></div>
      <div class="stat-label">Repeated clients</div>
    </div>
    <span class="abs stat-dot" style="left:475px;"></span>
    <div class="abs stat" style="left:542px; width:300px;">
      <div class="stat-value">100</div><div class="stat-rule"></div>
      <div class="stat-label">Percent of satisfied customers</div>
    </div>
    <span class="abs stat-dot" style="left:803px;"></span>
    <div class="abs stat" style="left:850px; width:252px;">
      <div class="stat-value">1</div><div class="stat-rule"></div>
      <div class="stat-label">Only one Tallow Bridge</div>
    </div>
  </div>
</section>

<section id="portfolio">
  <h2 class="abs section-title portfolio-title">Portfolio</h2>
  <div class="abs title-rule portfolio-rule"></div>
  <div class="abs brand portfolio-watermark" aria-hidden="true">
    <span class="brand-mark"></span>
    <span class="brand-name">TALLOW BRIDGE</span>
    <span class="brand-sub">(QLD) PTY LTD</span>
  </div>
  <div class="abs portfolio-grid">
    <div class="work-feature">
      <div class="work-feature-kicker">PROJECT FOR</div>
      <div class="brand">
        <span class="brand-mark"></span>
        <span class="brand-name">TALLOW BRIDGE</span>
        <span class="brand-sub">(QLD) PTY LTD</span>
      </div>
      <a class="work-feature-link" href="#portfolio">Browse whole project</a>
    </div>
    <div class="work-photo" role="img" aria-label="Photograph of a fitted-out office corridor with glazed walls"></div>
    <div class="work-photo" role="img" aria-label="Photograph of a fitted-out office corridor with glazed walls"></div>
    <div class="work-photo" role="img" aria-label="Photograph of a fitted-out office corridor with glazed walls"></div>
    <div class="work-photo" role="img" aria-label="Photograph of a fitted-out office corridor with glazed walls"></div>
    <div class="work-photo" role="img" aria-label="Photograph of a fitted-out office corridor with glazed walls"></div>
    <div class="work-photo" role="img" aria-label="Photograph of a fitted-out office corridor with glazed walls"></div>
    <div class="work-photo" role="img" aria-label="Photograph of a fitted-out office corridor with glazed walls"></div>
    <div class="work-photo" role="img" aria-label="Photograph of a fitted-out office corridor with glazed walls"></div>
    <div class="work-photo" role="img" aria-label="Photograph of a fitted-out office corridor with glazed walls"></div>
    <div class="work-photo" role="img" aria-label="Photograph of a fitted-out office corridor with glazed walls"></div>
    <div class="work-photo" role="img" aria-label="Photograph of a fitted-out office corridor with glazed walls"></div>
  </div>
</section>

<section id="contact">
  <h2 class="abs section-title contact-title">Contact</h2>
  <div class="abs title-rule contact-rule"></div>

  <form class="contact-form">
    <label class="abs field-label" style="left:52px; top:2452px;">First Name</label>
    <div class="abs field-box" style="left:48px; top:2484px; width:260px; height:42px;"></div>
    <label class="abs field-label" style="left:332px; top:2452px;">Last Name</label>
    <div class="abs field-box" style="left:330px; top:2484px; width:262px; height:42px;"></div>
    <label class="abs field-label" style="left:52px; top:2530px;">Email</label>
    <div class="abs field-box" style="left:48px; top:2560px; width:544px; height:42px;"></div>
    <label class="abs field-label" style="left:52px; top:2606px;">Company</label>
    <div class="abs field-box" style="left:48px; top:2636px; width:544px; height:42px;"></div>
    <label class="abs field-label" style="left:52px; top:2684px;">Message</label>
    <div class="abs field-box" style="left:48px; top:2714px; width:544px; height:130px;"></div>
  </form>

  <div class="abs brand contact-brand">
    <span class="brand-mark"></span>
    <span class="brand-name">TALLOW BRIDGE</span>
    <span class="brand-sub">(QLD) PTY LTD</span>
  </div>
  <address class="abs contact-details">
    <div>TALLOW BRIDGE (QLD) PTY LTD</div>
    <div>123 Exapmle Street , AB , USA</div>
    <div class="contact-line">
      <svg viewBox="0 0 20 20" aria-hidden="true"><rect x="5" y="1.5" width="10" height="17" rx="1.5" fill="none" stroke="#333" stroke-width="1.6"/><line x1="8.5" y1="15.5" x2="11.5" y2="15.5" stroke="#333" stroke-width="1.6"/></svg>
      <span>(1) 123 - 456 - 7890</span>
    </div>
    <div class="contact-line">
      <svg viewBox="0 0 20 20" aria-hidden="true"><rect x="1.5" y="4" width="17" height="12" fill="none" stroke="#333" stroke-width="1.6"/><polyline points="1.5,4 10,11 18.5,4" fill="none" stroke="#333" stroke-width="1.6"/></svg>
      <span>example@tallowbridge.com</span>
    </div>
  </address>
</section>

<footer class="abs site-footer">Copyright Tallow Bridge 2016 , All Rights Reserved</footer>

</body>
</html>
```